Optometry office needs a postcard to get name out to local schools

I need a postcard design for an optometry office called "Hosaru Optometry".
I want to get our name out to local schools and with this short letter and advertisement.
I want to keep the baby blue /navy blue colors theme.
One the front i want the following
Front:
1) three lines for the address of the recipient as in the example, and square for the postage in the upper right hand corner.
2) our logo with "Hosaru Optometry" and a horizontal line with our website address just below the line as in the example.
put the words "Our practice is committed to supporting our community and local schools." and our phone number "714-390-5264"
3) perhaps more contact info is looks neat and not too cluttered
Back:
1) letter which is attached
2) maybe a small clip art like a phoropter or glasses or something eye related

```html
<!DOCTYPE html>
<html lang="en">
<head>
<meta charset="utf-8">
<title>Hosaru Optometry Postcard</title>
<link rel="stylesheet" href="https://fonts.googleapis.com/css2?family=Mulish:wght@400;600;700&display=swap">
<style>
  :root {
    --navy: #2e3192;
    --deep-blue: #0f4c8c;
    --body-blue: #2170b8;
    --sky: #c9e0f3;
    --sky-light: #eef6fc;
    --ink: #3a3a3a;
    --rule: #3f4a4a;
    --paper: #ffffff;
    --backdrop: #ece8e2;
  }
  * { box-sizing: border-box; margin: 0; padding: 0; }
  html, body { width: 1200px; height: 1000px; overflow: hidden; }
  body {
    background: var(--backdrop);
    font-family: "Mulish", "Avenir", sans-serif;
    position: relative;
    color: var(--ink);
  }
  .card {
    position: absolute;
    background: var(--paper);
    box-shadow: 0 4px 14px rgba(0,0,0,0.25);
  }

  /* Address side */
  .card-front { left: 18px; top: 68px; width: 825px; height: 560px; }
  .brand-name {
    position: absolute; left: 62px; top: 62px;
    font-size: 44px; font-weight: 600; color: var(--navy);
    letter-spacing: 0.5px;
  }
  .brand-rule {
    position: absolute; left: 68px; top: 140px; width: 497px; height: 2px;
    background: var(--rule);
  }
  .website {
    position: absolute; left: 244px; top: 150px;
    font-size: 19px; letter-spacing: 2px; color: var(--ink);
  }
  .postage-box {
    position: absolute; left: 680px; top: 20px; width: 118px; height: 132px;
    border: 2px solid #111;
    display: flex; align-items: center; justify-content: center;
    text-align: center; font-size: 14px; color: #111; line-height: 1.25;
  }
  .tagline {
    position: absolute; left: 62px; top: 228px;
    font-size: 21px; line-height: 1.45; color: #555;
  }
  .phone {
    position: absolute; left: 58px; top: 372px;
    font-size: 28px; font-weight: 700; color: var(--navy); letter-spacing: 0.5px;
  }
  .contact {
    position: absolute; left: 56px; top: 414px;
    font-size: 14.5px; line-height: 1.55; color: #444; font-style: normal;
  }

  /* Letter side */
  .card-back { left: 338px; top: 348px; width: 832px; height: 604px; background: var(--body-blue); }
  .top-band { position: absolute; left: 0; top: 0; width: 100%; height: 18px; background: var(--deep-blue); }
  .hero {
    position: absolute; left: 0; top: 18px; width: 100%; height: 246px;
    background: linear-gradient(90deg, var(--sky-light) 0%, var(--sky) 60%, #b6d4ee 100%);
  }
  .logo-panel {
    position: absolute; left: 0; top: 64px; width: 318px; height: 140px;
    background: var(--paper); border-radius: 0 10px 10px 0;
    box-shadow: 2px 2px 6px rgba(0,0,0,0.15);
    display: flex; align-items: center; justify-content: center;
  }
  .logo-panel .brand-text {
    font-size: 33px; font-weight: 600; color: var(--navy); line-height: 1.1; text-align: center;
  }
  .hero-photo {
    position: absolute; left: 335px; top: 0; width: 497px; height: 246px;
    background: linear-gradient(90deg, rgba(255,255,255,0.55) 0%, #a9c3da 45%, #7d8894 70%, #b7cfe4 100%);
  }
  .letter {
    position: absolute; left: 64px; top: 286px; width: 742px;
    color: #fff; font-size: 15.2px; line-height: 1.32;
  }
  .letter p { margin-bottom: 9px; }
</style>
</head>
<body>

  <section class="card card-front" aria-label="Postcard address side">
    <div class="brand-name">Hosaru Optometry</div>
    <div class="brand-rule"></div>
    <div class="website">www.hosaruoptometry.com</div>
    <div class="postage-box">Postage<br>Area</div>
    <p class="tagline">Our practice is committed to supporting<br>our community and local schools.</p>
    <div class="phone">714-390-5264</div>
    <address class="contact">
      Hosaru Optometry<br>
      4120 Maple Grove Ave Ste B<br>
      Fairhaven, CA 90710<br>
      Email : hello@hosaruoptometry.com
    </address>
  </section>

  <section class="card card-back" aria-label="Postcard letter side">
    <div class="top-band"></div>
    <div class="hero">
      <div class="hero-photo" role="img" aria-label="Photo of an eye chart and a child looking through a phoropter during an eye exam"></div>
      <div class="logo-panel"><div class="brand-text">Hosaru Optometry</div></div>
    </div>
    <div class="letter">
      <p>Dear</p>
      <p>I would like to introduce our family optometry office that has been in business for the past 35 years! We are located at 4120 Maple Grove Ave Ste B in Fairhaven (near Maple Grove Ave and Harbor Rd).</p>
      <p>Our practice is committed to supporting our community and local schools by taking care of adults and children of all ages. As 80% of learning is done visually, it is especially important for young children to have access to routine comprehensive eye care. Our goal is to provide excellent eye care for families as well as quality ophthalmic frames and lenses at reasonable prices.</p>
      <p>We are happy to see any referrals from you, including students who have not passed vision screenings or have other ocular health concerns. Please feel free to reach out to us if you have any questions. You can contact us by phone or email, and are also welcome to visit our office anytime.</p>
      <p>We look forward to a strong relationship together and success for all your students.</p>
      <p>Sincerely</p>
      <p>Kenji Hosaru, OD</p>
    </div>
  </section>

</body>
</html>
```